Web Design Project

We are re-starting this project.

This project is for a totally new look and design of a website for Wablor. www.wablor-demo.net.

Wablor is a naming protocol for physical locations and can be used for fixed and mobile people, places and things. Find your friends, or find a business. Because Wablor locations point to precise geo-physical (GPS) co-ordinates, navigation to a location becomes totally reliable.
Updates

Please see the modified brief for this project

Target Market(s)

Every person and every business can have multiple !Wabs (Wablor locations), so the website needs to be appealing and fun, but easy to use and functional

Industry/Entity Type

Business

Colors
34a6d7

Requirements
Must have
• Uniqueness!

```html
<!DOCTYPE html>
<html lang="en">
<head>
<meta charset="utf-8">
<title>Wablor – Find people, places and things</title>
<link rel="stylesheet" href="https://fonts.googleapis.com/css2?family=PT+Sans+Narrow:wght@400;700&family=PT+Sans:wght@400;700&display=swap">
<style>
:root{
  --brand:#34a6d7;
  --nav:#1f99d5;
  --nav-line:#17618a;
  --btn-dark:#102a40;
  --hero-top:#2b3137;
  --hero-bottom:#1f2429;
  --rule:#2a6f9c;
  --white:#ffffff;
  --band:#036397;
  --circle:#1f9ad6;
  --footer:#1c4b6c;
  --social:#5cc0ec;
  --input:#ebe6e7;
  --input-border:#1b4460;
}
*{box-sizing:border-box;margin:0;padding:0}
html,body{width:1200px;height:1068px;overflow:hidden}
body{position:relative;font-family:"PT Sans Narrow",sans-serif;color:var(--white);background:var(--band)}

.site-nav{position:absolute;left:0;top:0;width:1200px;height:65px;background:var(--nav);border-bottom:2px solid #17709e}
.nav-link{position:absolute;top:21px;transform:translateX(-50%);font-size:19px;font-weight:700;color:var(--white);text-decoration:none;letter-spacing:.2px}
.nav-sep{position:absolute;top:12px;width:2px;height:40px;background:var(--nav-line);border-radius:2px}
.nav-btn{position:absolute;top:13px;height:37px;width:114px;border-radius:7px;background:var(--btn-dark);color:var(--white);font-size:19px;font-weight:700;text-align:center;line-height:37px;text-decoration:none}

.hero{position:absolute;left:0;top:65px;width:1200px;height:643px}
.hero-bg{position:absolute;inset:0;background:radial-gradient(ellipse at 45% 35%,#3a4148 0%,var(--hero-top) 45%,var(--hero-bottom) 100%)}
.hero-logo{position:absolute;left:0;width:1200px;top:70px;text-align:center;font-family:"PT Sans",sans-serif;font-weight:700;font-size:66px;color:var(--brand);letter-spacing:-1px}
.hero-rule{position:absolute;left:323px;width:578px;height:4px;background:var(--rule)}
.hero-title{position:absolute;left:0;width:1200px;top:242px;text-align:center;font-size:30px;font-weight:700;letter-spacing:.2px}
.hero-sub{position:absolute;left:0;width:1200px;top:286px;text-align:center;font-size:27px;font-weight:400}
.find-title{position:absolute;left:0;width:1200px;top:412px;text-align:center;font-size:44px;font-weight:700;color:var(--brand)}
.find-hints{position:absolute;top:487px;left:0;width:1200px;font-size:21px}
.hint{position:absolute;display:flex;align-items:center;gap:6px;white-space:nowrap}
.hint svg{width:28px;height:12px}
.search-field{position:absolute;left:333px;top:532px;width:478px;height:66px;border:3px solid var(--input-border);border-radius:8px;background:var(--input);font-family:"PT Sans",sans-serif;font-size:22px;color:#222;padding:0 12px;line-height:60px}
.search-btn{position:absolute;left:826px;top:529px;width:87px;height:70px;border:3px solid #3e4a55;border-radius:8px;background:var(--brand);display:flex;align-items:center;justify-content:center}

.activity{position:absolute;left:24px;top:708px;width:1152px;height:302px;display:grid;grid-template-columns:repeat(6,192px)}
.person{display:flex;flex-direction:column;align-items:center;text-align:center}
.person-name{margin-top:49px;font-size:20px;font-weight:400;letter-spacing:.2px}
.timer{margin-top:9px;width:88px;height:88px;border-radius:50%;background:var(--circle);position:relative;display:flex;flex-direction:column;align-items:center;justify-content:center;line-height:1}
.timer::after{content:"";position:absolute;inset:4px;border:2px dashed rgba(255,255,255,.55);border-radius:50%}
.timer-value{font-size:28px;font-family:"PT Sans",sans-serif}
.timer-unit{font-size:16px;font-family:"PT Sans",sans-serif;margin-top:3px}
.person-loc{margin-top:12px;font-family:"PT Sans",sans-serif;font-size:16px;line-height:21px}
.person-actions{margin-top:9px;display:flex;gap:9px;align-items:center}

.site-footer{position:absolute;left:0;top:1010px;width:1200px;height:58px;background:var(--footer)}
.footer-logo{position:absolute;left:14px;top:10px;font-family:"PT Sans",sans-serif;font-weight:700;font-size:30px;color:var(--white)}
.social{position:absolute;top:12px;width:34px;height:34px;border-radius:50%;background:var(--social)}
</style>
</head>
<body>

<nav class="site-nav">
  <a class="nav-link" style="left:44px" href="#">HOME</a>
  <span class="nav-sep" style="left:94px"></span>
  <a class="nav-link" style="left:151px" href="#">ABOUT</a>
  <span class="nav-sep" style="left:204px"></span>
  <a class="nav-link" style="left:252px" href="#">HELP</a>
  <span class="nav-sep" style="left:297px"></span>
  <a class="nav-link" style="left:358px" href="#">CONTACT</a>
  <span class="nav-sep" style="left:420px"></span>
  <a class="nav-link" style="left:481px" href="#">PRIVACY</a>
  <span class="nav-sep" style="left:542px"></span>
  <a class="nav-link" style="left:592px" href="#">TERMS</a>
  <span class="nav-sep" style="left:646px"></span>
  <a class="nav-link" style="left:718px" href="#">REFUNDS</a>
  <span class="nav-sep" style="left:788px"></span>
  <a class="nav-link" style="left:839px" href="#">FAQ</a>
  <a class="nav-btn" style="left:940px" href="#">SIGNUP</a>
  <a class="nav-btn" style="left:1068px" href="#">LOGIN</a>
</nav>

<header class="hero">
  <div class="hero-bg" role="img" aria-label="Darkened photo of a smartphone lying on a printed city street map"></div>
  <div class="hero-logo">Wablor</div>
  <div class="hero-rule" style="top:202px"></div>
  <h1 class="hero-title">WABLOR IS THE FIRST NEW ADDRESS SYSTEM FOR PHYSICAL LOCATIONS</h1>
  <p class="hero-sub">SINCE WE ALL RODE AROUND ON HORSES!</p>
  <div class="hero-rule" style="top:348px"></div>
  <h2 class="find-title">WHO WOULD YOU LIKE TO FIND?</h2>
  <div class="find-hints">
    <span class="hint" style="left:338px"><svg viewBox="0 0 28 12"><path d="M1 6h24M19 1l6 5-6 5" fill="none" stroke="#34a6d7" stroke-width="2"/></svg>In these Catrgories</span>
    <span class="hint" style="left:532px"><svg viewBox="0 0 28 12"><path d="M1 6h24M19 1l6 5-6 5" fill="none" stroke="#34a6d7" stroke-width="2"/></svg>With these keywords</span>
    <span class="hint" style="left:750px"><svg viewBox="0 0 28 12"><path d="M1 6h24M19 1l6 5-6 5" fill="none" stroke="#34a6d7" stroke-width="2"/></svg>Closet to this place</span>
  </div>
  <div class="search-field">Find Wab....</div>
  <div class="search-btn">
    <svg width="56" height="52" viewBox="0 0 56 52"><circle cx="22" cy="21" r="14" fill="none" stroke="#fff" stroke-width="6"/><path d="M32 31l16 15" stroke="#fff" stroke-width="8" stroke-linecap="round"/></svg>
  </div>
</header>

<section class="activity">
  <div class="person"><div class="person-name">JORDANPKELLAWAY</div><div class="timer"><span class="timer-value">13</span><span class="timer-unit">seconds</span></div><div class="person-loc">current location<br>!JORDANPKELLAWAY</div><div class="person-actions"><svg width="18" height="26" viewBox="0 0 18 26"><path d="M9 1a8 8 0 0 1 8 8c0 6-8 16-8 16S1 15 1 9a8 8 0 0 1 8-8z" fill="#fff"/><circle cx="9" cy="9" r="3" fill="#036397"/></svg><svg width="26" height="26" viewBox="0 0 26 26"><circle cx="13" cy="13" r="11" fill="none" stroke="#fff" stroke-width="2.5"/><path d="M18 8l-3 7-7 3 3-7z" fill="#fff"/></svg></div></div>
  <div class="person"><div class="person-name">JORDANPKELLAWAY</div><div class="timer"><span class="timer-value">16</span><span class="timer-unit">seconds</span></div><div class="person-loc">current location<br>!JORDANPKELLAWAY</div><div class="person-actions"><svg width="18" height="26" viewBox="0 0 18 26"><path d="M9 1a8 8 0 0 1 8 8c0 6-8 16-8 16S1 15 1 9a8 8 0 0 1 8-8z" fill="#fff"/><circle cx="9" cy="9" r="3" fill="#036397"/></svg><svg width="26" height="26" viewBox="0 0 26 26"><circle cx="13" cy="13" r="11" fill="none" stroke="#fff" stroke-width="2.5"/><path d="M18 8l-3 7-7 3 3-7z" fill="#fff"/></svg></div></div>
  <div class="person"><div class="person-name">JORDANPKELLAWAY</div><div class="timer"><span class="timer-value">28</span><span class="timer-unit">seconds</span></div><div class="person-loc">current location<br>!JORDANPKELLAWAY</div><div class="person-actions"><svg width="18" height="26" viewBox="0 0 18 26"><path d="M9 1a8 8 0 0 1 8 8c0 6-8 16-8 16S1 15 1 9a8 8 0 0 1 8-8z" fill="#fff"/><circle cx="9" cy="9" r="3" fill="#036397"/></svg><svg width="26" height="26" viewBox="0 0 26 26"><circle cx="13" cy="13" r="11" fill="none" stroke="#fff" stroke-width="2.5"/><path d="M18 8l-3 7-7 3 3-7z" fill="#fff"/></svg></div></div>
  <div class="person"><div class="person-name">JORDANPKELLAWAY</div><div class="timer"><span class="timer-value">2</span><span class="timer-unit">Minutes</span></div><div class="person-loc">current location<br>!JORDANPKELLAWAY</div><div class="person-actions"><svg width="18" height="26" viewBox="0 0 18 26"><path d="M9 1a8 8 0 0 1 8 8c0 6-8 16-8 16S1 15 1 9a8 8 0 0 1 8-8z" fill="#fff"/><circle cx="9" cy="9" r="3" fill="#036397"/></svg><svg width="26" height="26" viewBox="0 0 26 26"><circle cx="13" cy="13" r="11" fill="none" stroke="#fff" stroke-width="2.5"/><path d="M18 8l-3 7-7 3 3-7z" fill="#fff"/></svg></div></div>
  <div class="person"><div class="person-name">JORDANPKELLAWAY</div><div class="timer"><span class="timer-value">10</span><span class="timer-unit">Minutes</span></div><div class="person-loc">current location<br>!JORDANPKELLAWAY</div><div class="person-actions"><svg width="18" height="26" viewBox="0 0 18 26"><path d="M9 1a8 8 0 0 1 8 8c0 6-8 16-8 16S1 15 1 9a8 8 0 0 1 8-8z" fill="#fff"/><circle cx="9" cy="9" r="3" fill="#036397"/></svg><svg width="26" height="26" viewBox="0 0 26 26"><circle cx="13" cy="13" r="11" fill="none" stroke="#fff" stroke-width="2.5"/><path d="M18 8l-3 7-7 3 3-7z" fill="#fff"/></svg></div></div>
  <div class="person"><div class="person-name">JORDANPKELLAWAY</div><div class="timer"><span class="timer-value">25</span><span class="timer-unit">Minutes</span></div><div class="person-loc">current location<br>!JORDANPKELLAWAY</div><div class="person-actions"><svg width="18" height="26" viewBox="0 0 18 26"><path d="M9 1a8 8 0 0 1 8 8c0 6-8 16-8 16S1 15 1 9a8 8 0 0 1 8-8z" fill="#fff"/><circle cx="9" cy="9" r="3" fill="#036397"/></svg><svg width="26" height="26" viewBox="0 0 26 26"><circle cx="13" cy="13" r="11" fill="none" stroke="#fff" stroke-width="2.5"/><path d="M18 8l-3 7-7 3 3-7z" fill="#fff"/></svg></div></div>
</section>

<footer class="site-footer">
  <div class="footer-logo">Wablor</div>
  <a class="social" style="left:968px" href="#" aria-label="Social link 1"></a>
  <a class="social" style="left:1013px" href="#" aria-label="Social link 2"></a>
  <a class="social" style="left:1060px" href="#" aria-label="News feed"></a>
  <a class="social" style="left:1107px" href="#" aria-label="Social link 3"></a>
  <a class="social" style="left:1152px" href="#" aria-label="Social link 4"></a>
</footer>

</body>
</html>
```